wine label design

i'm a fine wine store based in new zealand which buys quality bulk wine and bottles it, passing on the significant savings onto the customer. i require a brand name and design which is cool/ sharp and contempory. the wines will be all still wines, there won't be any sparkling wines under this brand. i've used brand names like harbourlight wine company for previous designs/label but want something more edgier. we thought about a brand name 'sky above the vines' or 'harbourlight wine co' but couldn't get a design to match the title of brand, if you have any thoughts on this send thru your design. take into account color they have to be bold as i am printing these thru a digital printer. the label is a wrap around design, the dimensions are approximately 80 or 90 mm high and 210 mm wide. have a look at these links, i think they have some x-factor to them: http://www.marlowvale.example/store/product_images/p/855/velora__34476_zoom.jpg: OR

http://static3.cellarfinder.example/images/labels/35/24/ember-in-the-fog-shiraz-petite-sirah-south-australia-10203524.jpg: OR

http://www.bottlebarn.example/ui/productimages/25223/25223_w240.jpg: OR

http://www.vintrail.example/images/viewWinery.php?pic=238291

Take into account i have to be able put a wine desription on the back label, barcode and a few technical details required by law. on the front label all i require is space to put the grape variety, area and vintage. i need the grape type to really stand out.
Updates

Reason: hi, the designs coming thru look good, just need a little more changes, also please read thru the brief, there are a few things i have noted such as label size etc etc

Target Market(s)

am after a label the cool/edgy/contempoary that appeals to the educated well off customer that willing to give something new a go by the look of the label that is cool and edgy.

Industry/Entity Type

Boutique

Requirements
Must have
• bold bold bold, it must stand out on the shelf
Nice to have
• a title/brand name that links what i'm doing, from what i'm doing the name 'harbourlight wine co' is probably best suited.
Should not have
• basic boring artwork and small text, the bigger the text the better

```html
<!DOCTYPE html>
<html lang="en">
<head>
<meta charset="utf-8">
<title>Harbourlight Wine Co: Chenin Blanc Label</title>
<link rel="stylesheet" href="https://fonts.googleapis.com/css2?family=Marcellus&display=swap">
<style>
  :root {
    --label-black: #000000;
    --brand-white: #ffffff;
    --leaf-green: #a6e51f;
    --leaf-green-deep: #8fd40f;
    --leaf-green-light: #f1fbe0;
    --leaf-grey-light: #5a5a5a;
    --leaf-grey-dark: #1c1c1c;
    --variety-ink: #0d0d0d;
  }
  html, body {
    margin: 0;
    padding: 0;
    width: 1200px;
    height: 516px;
    overflow: hidden;
    background: var(--label-black);
  }
  .label {
    position: relative;
    width: 1200px;
    height: 516px;
    background: var(--label-black);
    overflow: hidden;
    font-family: "Marcellus", serif;
  }

  /* Brand name */
  .brand {
    position: absolute;
    right: 395px;
    top: 96px;
    margin: 0;
    text-align: right;
    color: var(--brand-white);
    font-weight: 400;
    text-transform: uppercase;
    line-height: 1;
    white-space: nowrap;
  }
  .brand__line {
    display: block;
    font-size: 66px;
    letter-spacing: 3px;
  }
  .brand__line + .brand__line {
    margin-top: 30px;
  }
  .brand__co {
    font-size: 34px;
    margin-left: 22px;
    letter-spacing: 2px;
  }

  /* Vine leaf artwork areas */
  .vine-leaf {
    position: absolute;
    background: radial-gradient(ellipse at 45% 40%, var(--leaf-grey-light) 0%, var(--leaf-grey-dark) 75%, transparent 100%);
  }
  .vine-leaf--far-left {
    left: 184px; top: 335px; width: 168px; height: 200px;
    border-radius: 48% 44% 30% 40% / 40% 46% 40% 44%;
    transform: rotate(-10deg);
  }
  .vine-leaf--centre {
    left: 580px; top: 368px; width: 136px; height: 170px;
    border-radius: 46% 50% 34% 40% / 44% 46% 40% 40%;
    transform: rotate(8deg);
  }
  .vine-leaf--tall {
    left: 697px; top: 284px; width: 186px; height: 250px;
    border-radius: 50% 50% 36% 40% / 46% 46% 40% 40%;
  }
  .vine-leaf--far-right {
    left: 836px; top: 335px; width: 174px; height: 200px;
    border-radius: 44% 50% 38% 34% / 42% 46% 40% 40%;
    transform: rotate(6deg);
  }
  .variety-leaf {
    position: absolute;
    left: 312px;
    top: 224px;
    width: 300px;
    height: 300px;
    border-radius: 30% 58% 40% 52% / 26% 48% 50% 56%;
    transform: rotate(-8deg);
    background: radial-gradient(circle at 40% 60%, var(--leaf-green-light) 0%, var(--leaf-green) 55%, var(--leaf-green-deep) 100%);
  }

  /* Wine details */
  .variety {
    position: absolute;
    left: 345px;
    top: 318px;
    width: 240px;
    margin: 0;
    color: var(--variety-ink);
    transform: rotate(-20deg);
    transform-origin: center;
    text-align: center;
    text-transform: uppercase;
    line-height: 1;
    white-space: nowrap;
  }
  .variety__vintage {
    display: block;
    font-size: 18px;
    margin-left: -120px;
  }
  .variety__grape {
    display: block;
    font-size: 27px;
    margin-top: 6px;
    letter-spacing: 1px;
  }
  .variety__region {
    display: block;
    font-size: 16px;
    margin-top: 5px;
    letter-spacing: 1.5px;
  }
</style>
</head>
<body>
  <main class="label">
    <h1 class="brand">
      <span class="brand__line">Harbourlight</span>
      <span class="brand__line">Wine<span class="brand__co">co</span></span>
    </h1>

    <div class="vine-leaf vine-leaf--far-left" role="img" aria-label="Dark grey vine leaf"></div>
    <div class="vine-leaf vine-leaf--centre" role="img" aria-label="Dark grey vine leaf"></div>
    <div class="vine-leaf vine-leaf--tall" role="img" aria-label="Dark grey vine leaf"></div>
    <div class="vine-leaf vine-leaf--far-right" role="img" aria-label="Dark grey vine leaf"></div>

    <div class="variety-leaf" role="img" aria-label="Bright green vine leaf carrying the wine details"></div>

    <p class="variety">
      <span class="variety__vintage">2005</span>
      <span class="variety__grape">Chenin Blanc</span>
      <span class="variety__region">Tidewater</span>
    </p>
  </main>
</body>
</html>
```